Business Card for Industrial Distributor

We need a business card design for an industrial distributor. We sell machine parts for the manufacturing and oil industry. We would like the cards to look clean and modern but with a touch of industry.

Our colors are blue/white.

Please feel free to visit our website www.krovelmint.com

Target Market(s)

mexican manufacturers in the automobile/aerospace industry

Industry/Entity Type

Industrial

Colors
ffffff
0555a3

```html
<!DOCTYPE html>
<html lang="en">
<head>
<meta charset="utf-8">
<title>Krovelmint Business Card</title>
<link href="https://fonts.googleapis.com/css2?family=Lato:wght@400;700&display=swap" rel="stylesheet">
<style>
  :root {
    --brand-blue: #3d4897;
    --paper: #ffffff;
    --outline: #3a3a3a;
    --contact-grey: #6b6b6b;
  }
  html, body {
    margin: 0;
    padding: 0;
    width: 1200px;
    height: 761px;
    overflow: hidden;
    background: var(--paper);
    font-family: "Lato", sans-serif;
  }
  .canvas {
    position: relative;
    width: 1200px;
    height: 761px;
  }
  .card {
    position: absolute;
    top: 214px;
    width: 459px;
    height: 298px;
    box-sizing: border-box;
    border: 1px solid var(--outline);
    background: var(--paper);
    overflow: hidden;
  }
  .card--front { left: 145px; }
  .card--back { left: 619px; }

  .band {
    position: absolute;
    background: var(--brand-blue);
  }
  .card--front .band { left: 24px; width: 174px; }
  .card--front .band--top { top: 0; height: 123px; }
  .card--front .band--bottom { top: 177px; height: 121px; }

  .card--back .band { left: 75px; width: 309px; }
  .card--back .band--top { top: 0; height: 119px; }
  .card--back .band--bottom { top: 191px; height: 107px; }

  .brand {
    position: absolute;
    display: flex;
    align-items: center;
    color: var(--brand-blue);
    font-weight: 700;
    white-space: nowrap;
  }
  .brand__dot {
    border-radius: 50%;
    background: var(--brand-blue);
    flex: none;
  }
  .card--front .brand { left: 26px; top: 131px; height: 36px; font-size: 21px; gap: 6px; }
  .card--front .brand__dot { width: 32px; height: 32px; }
  .card--back .brand { left: 78px; top: 124px; height: 62px; font-size: 42px; gap: 10px; }
  .card--back .brand__dot { width: 58px; height: 58px; }

  .contact {
    position: absolute;
    right: 26px;
    top: 218px;
    margin: 0;
    padding: 0;
    list-style: none;
    text-align: right;
    color: var(--contact-grey);
    font-size: 14.5px;
    line-height: 21.5px;
  }
  .back-web {
    position: absolute;
    left: 75px;
    width: 309px;
    top: 268px;
    text-align: center;
    color: var(--paper);
    font-size: 14.5px;
  }
</style>
</head>
<body>
<div class="canvas">
  <section class="card card--front">
    <div class="band band--top"></div>
    <div class="brand"><span class="brand__dot"></span>Krovelmint</div>
    <div class="band band--bottom"></div>
    <ul class="contact">
      <li>+333 22 468 3590</li>
      <li>info@krovelmint.com</li>
      <li>www.krovelmint.com</li>
    </ul>
  </section>

  <section class="card card--back">
    <div class="band band--top"></div>
    <div class="brand"><span class="brand__dot"></span>Krovelmint</div>
    <div class="band band--bottom"></div>
    <div class="back-web">www.krovelmint.com</div>
  </section>
</div>
</body>
</html>
```